32 Years Old Company Needs More Attractive Label and Packaging Design

Our company has come out with upgraded ingredients for our current product. We are producing flavored concentrate drinks since 1982. Our intention here is to have a new label and packaging design for this to be launched product - rose syrup. We would like to see the wording 'Natural Color' and 'No added preservative' to be highlighted and not to forget our registered brand name is 'Kolvi'. We intend to use shrink wrap around label and photos of our current label and type of bottle including the size and color as per attachment.

Pls take note , for the new label will be shrink wrap not as existing label shown in picture.

Industry/Entity Type

It Company

```html
<!DOCTYPE html>
<html lang="en">
<head>
<meta charset="utf-8">
<title>Kolvi Rose Syrup – Label Design</title>
<link href="https://fonts.googleapis.com/css2?family=Alfa+Slab+One&family=Russo+One&display=swap" rel="stylesheet">
<style>
  :root {
    --bg: #1a0b07;
    --red: #e41f26;
    --deep-red: #c8141c;
    --orange: #f58a1f;
    --amber: #f7a823;
    --plum: #4e0b2b;
    --white: #ffffff;
  }
  * { margin: 0; padding: 0; box-sizing: border-box; }
  html, body { width: 1200px; height: 1000px; overflow: hidden; }
  body {
    background: radial-gradient(ellipse at 50% 40%, #2a130c 0%, var(--bg) 70%);
    position: relative;
    font-family: "Russo One", sans-serif;
  }
  .brand-card {
    position: absolute; left: 462px; top: 117px;
    width: 292px; height: 185px; background: var(--white);
    display: flex; flex-direction: column; align-items: center; padding-top: 18px;
  }
  .brand-name {
    font-family: "Russo One", sans-serif; font-size: 30px; color: var(--red); line-height: 1;
  }
  .since { font-size: 7px; color: var(--deep-red); margin-top: 8px; letter-spacing: .5px; }
  .title-row { display: flex; align-items: center; gap: 14px; margin-top: 6px; }
  .rose-art { width: 34px; height: 34px; border-radius: 50%; }
  .rose-art.warm { background: radial-gradient(circle, var(--orange), var(--red)); }
  .rose-art.gold { background: radial-gradient(circle, var(--amber), var(--orange)); }
  .product-title {
    font-family: "Alfa Slab One", serif; color: var(--red); text-align: center;
    line-height: .95; transform: scaleX(.78);
  }
  .brand-card .product-title { font-size: 40px; }
  .brand-card .product-title .line2 { display: block; }

  .label { position: absolute; top: 322px; width: 304px; height: 302px; }
  .label.light { left: 288px; }
  .label.dark { left: 607px; }
  .label svg.shape { position: absolute; inset: 0; }
  .label-content {
    position: absolute; inset: 0; display: flex; flex-direction: column; align-items: center;
  }
  .label .brand-name { margin-top: 34px; font-size: 28px; }
  .label.dark .brand-name { color: var(--red); }
  .label .since { margin-top: 10px; }
  .label.dark .since { color: #f2b0b0; }
  .label .rose-art { position: absolute; top: 58px; width: 74px; height: 74px; }
  .label .rose-art.left { left: 20px; }
  .label .rose-art.right { right: 20px; }
  .label .product-title { font-size: 50px; margin-top: 12px; }
  .label .product-title span { display: block; }
  .claims {
    position: absolute; left: 0; right: 0; top: 215px;
    text-align: center; color: var(--white);
  }
  .claim-main { font-size: 16px; letter-spacing: .5px; }
  .claim-sub { font-size: 10px; margin-top: 8px; }
  .volume { font-size: 8px; margin-top: 10px; }
</style>
</head>
<body>

  <section class="brand-card">
    <div class="brand-name">Kolvi</div>
    <div class="since">SINCE 1982</div>
    <div class="title-row">
      <div class="rose-art warm" role="img" aria-label="Rose flower illustration"></div>
      <div class="product-title">ROSE<span class="line2">SYRUP</span></div>
      <div class="rose-art gold" role="img" aria-label="Rose flower illustration"></div>
    </div>
  </section>

  <section class="label light">
    <svg class="shape" viewBox="0 0 304 302" width="304" height="302">
      <defs>
        <linearGradient id="frameLight" x1="0" x2="1"><stop offset="0" stop-color="#f7a823"/><stop offset="1" stop-color="#e9421f"/></linearGradient>
        <linearGradient id="bandLight" x1="0" x2="1"><stop offset="0" stop-color="#f7a823"/><stop offset="1" stop-color="#f06a1e"/></linearGradient>
      </defs>
      <path d="M0,50 H60 Q74,0 152,0 Q230,0 244,50 H304 V302 H0 Z" fill="url(#frameLight)"/>
      <path d="M7,56 H65 Q78,7 152,7 Q226,7 239,56 H297 V295 H7 Z" fill="#ffffff"/>
      <rect x="7" y="203" width="290" height="92" fill="url(#bandLight)"/>
      <rect x="12" y="208" width="280" height="82" fill="none" stroke="#ffffff" stroke-opacity=".6"/>
    </svg>
    <div class="label-content">
      <div class="brand-name">Kolvi</div>
      <div class="since">SINCE 1982</div>
      <div class="product-title"><span>ROSE</span><span>SYRUP</span></div>
    </div>
    <div class="rose-art warm left" role="img" aria-label="Rose flower illustration"></div>
    <div class="rose-art gold right" role="img" aria-label="Rose flower illustration"></div>
    <div class="claims">
      <div class="claim-main">NATURAL COLOR</div>
      <div class="claim-sub">NO ADDED PRESERVATIVE</div>
      <div class="volume">375 ML</div>
    </div>
  </section>

  <section class="label dark">
    <svg class="shape" viewBox="0 0 304 302" width="304" height="302">
      <defs>
        <linearGradient id="frameDark" x1="0" x2="1"><stop offset="0" stop-color="#f7a823"/><stop offset="1" stop-color="#e9421f"/></linearGradient>
        <linearGradient id="bandDark" x1="0" x2="1"><stop offset="0" stop-color="#f06a2a"/><stop offset="1" stop-color="#e21f34"/></linearGradient>
      </defs>
      <path d="M0,50 H60 Q74,0 152,0 Q230,0 244,50 H304 V302 H0 Z" fill="url(#frameDark)"/>
      <path d="M7,56 H65 Q78,7 152,7 Q226,7 239,56 H297 V295 H7 Z" fill="#4e0b2b"/>
      <rect x="7" y="203" width="290" height="92" fill="url(#bandDark)"/>
    </svg>
    <div class="label-content">
      <div class="brand-name">Kolvi</div>
      <div class="since">SINCE 1982</div>
      <div class="product-title"><span>ROSE</span><span>SYRUP</span></div>
    </div>
    <div class="rose-art warm left" role="img" aria-label="Rose flower illustration"></div>
    <div class="rose-art gold right" role="img" aria-label="Rose flower illustration"></div>
    <div class="claims">
      <div class="claim-main">NATURAL COLOR</div>
      <div class="claim-sub">NO ADDED PRESERVATIVE</div>
      <div class="volume">375 ML</div>
    </div>
  </section>

</body>
</html>
```